Fun, cartoonish website design wanted

crazy fun design wanted!
design and upload/install a creative, unique, fun site that will be used within wordpress/woocommerce for our new business concept otterbites.store where we will be selling immune system boosters, vitamins and work out supplements. We would like the theme to be fun and the designer to really use their creativity with considering a possible cartoonish style design. Although a single page we would want the page to look very clean, catchy and custom. We are trying to portray by using the name otter bites that the vitamins/supplements we are selling are strong, please keep that in mind for the design. any questions please feel free to contact me asap. again we are looking for pro's to get creative and work their magic!

Target Market(s)

health & fitness

Industry/Entity Type

Health And Wellness

Coding

Coded - Design and coding required

Number of Pages Required

3 page

Requirements
Must have
• very unique and creative
clean and flow easy for sales
one page as shop page that will host multiple products.
custom navigation bar / buttons
cool checkout page
Nice to have
• more creative the better

```html
<!DOCTYPE html>
<html lang="en">
<head>
<meta charset="utf-8">
<title>Otter Bites — Natural Supplements</title>
<link href="https://fonts.googleapis.com/css2?family=Lato:ital,wght@0,300;0,400;0,700;0,900;1,300&display=swap" rel="stylesheet">
<style>
:root{
  --green:#046a04;
  --green-tab:#4a8a2c;
  --beige:#f3f0e9;
  --ink:#2b2b2b;
  --muted:#7a7a7a;
  --white:#ffffff;
  --cream:#f7f2c4;
  --star:#f5b300;
}
*{margin:0;padding:0;box-sizing:border-box}
html,body{width:1200px;height:2491px;overflow:hidden;background:var(--white)}
body{position:relative;font-family:'Lato',sans-serif;color:var(--ink)}
.abs{position:absolute}

/* header + hero */
.hero{position:absolute;left:0;top:0;width:1200px;height:600px;overflow:hidden}
.hero-bg{position:absolute;inset:0}
.hero-art{position:absolute;left:780px;top:80px;width:400px;height:500px;border-radius:8px;
  background:linear-gradient(180deg,#5d7a63 0%,#3f5670 45%,#2b3c57 100%)}
.logo{left:150px;top:18px;font-size:26px;font-weight:700;color:var(--green)}
.nav{left:484px;top:24px;display:flex;gap:26px;font-size:14px;font-weight:700;color:var(--ink)}
.icons{left:921px;top:22px;display:flex;gap:18px}
.cart-count{position:absolute;left:1036px;top:18px;font-size:9px}
.hero-title{left:150px;top:222px;font-size:37px;font-weight:900;line-height:44px;color:var(--green)}
.hero-sub{left:150px;top:314px;font-size:29px;font-weight:700;line-height:38px;color:var(--ink)}
.btn{display:flex;align-items:center;justify-content:center;background:var(--green);color:var(--white);
  font-size:12px;font-weight:700;border-radius:20px}
.hero-btn{left:150px;top:400px;width:136px;height:38px}

/* perks band */
.perks{left:0;top:600px;width:1200px;height:113px}
.perk{position:absolute;top:638px;font-size:28px;font-weight:700;width:360px;text-align:center}

/* categories */
.cat{position:absolute;top:752px;width:292px;height:292px;box-shadow:0 2px 5px rgba(0,0,0,.2)}
.cat-label{position:absolute;left:0;top:128px;width:100%;height:37px;background:var(--white);
  display:flex;align-items:center;justify-content:center;font-size:21px;color:var(--ink)}

/* tabs */
.tabs{left:0;top:1083px;width:1200px;height:68px;background:var(--green)}
.tab{position:absolute;top:0;height:68px;width:300px;display:flex;align-items:center;justify-content:center;
  font-size:28px;font-weight:300;color:var(--white)}
.tab.active{background:var(--green-tab)}

/* products */
.card{position:absolute;width:293px;height:417px;background:var(--beige);box-shadow:0 2px 6px rgba(0,0,0,.12)}
.card-img{position:absolute;left:0;top:0;width:100%;height:187px;background:var(--white)}
.bottle{position:absolute;left:107px;top:20px;width:80px;height:150px;border-radius:10px 10px 6px 6px}
.bottle.orange{background:linear-gradient(90deg,#f48a00,#ffa21a 50%,#f48a00)}
.bottle.yellow{background:linear-gradient(180deg,#2a1a1a 0 22%,#f2e05a 22%,#f6e46a 92%,#2a1a1a 92%)}
.card-title{position:absolute;left:16px;top:206px;font-size:21px;font-weight:400;color:var(--ink)}
.card-price{position:absolute;right:15px;top:206px;font-size:19px;color:var(--ink)}
.card-desc{position:absolute;left:17px;top:242px;width:262px;font-size:13px;line-height:20px;font-weight:300;color:var(--muted)}
.rating{position:absolute;left:78px;top:328px;display:flex;align-items:center;gap:3px;font-size:10px;color:var(--ink)}
.card-btn{position:absolute;left:78px;top:358px;width:136px;height:37px}

/* newsletter */
.news{left:0;top:2069px;width:1200px;height:182px;background:var(--green)}
.news-art{left:930px;top:2045px;width:250px;height:190px;border-radius:8px;
  background:linear-gradient(180deg,#4f627f,#2b3c57)}
.news-title{left:150px;top:2100px;font-size:29px;font-weight:700;color:var(--white)}
.news-sub{left:150px;top:2138px;font-size:21px;color:var(--white)}
.news-input{left:150px;top:2177px;width:262px;height:37px;background:var(--white);border-radius:19px;
  padding-left:15px;display:flex;align-items:center;font-size:11px;font-style:italic;font-weight:300;color:var(--muted)}
.news-btn{left:420px;top:2177px;width:136px;height:37px;background:var(--cream);color:var(--ink)}

/* footer */
.foot-logo{left:150px;top:2286px;font-size:26px;font-weight:700;color:var(--green)}
.foot-about{left:154px;top:2321px;width:260px;font-size:13px;line-height:20px;color:var(--ink)}
.foot-h{font-size:16px;color:var(--ink)}
.foot-links{font-size:13px;line-height:27px;color:var(--ink)}
.social{left:922px;top:2319px;display:flex;gap:8px}
.social span{width:37px;height:37px;border-radius:50%;background:var(--green);display:block}
.copyright{left:0;top:2452px;width:1200px;height:39px;background:var(--beige);display:flex;
  align-items:center;justify-content:center;font-size:13px;color:var(--ink)}
</style>
</head>
<body>

<section class="hero">
  <svg class="hero-bg" width="1200" height="600"><polygon points="812,0 1200,0 1200,600 401,600" fill="#f3f0e9"/></svg>
  <div class="hero-art" role="img" aria-label="Illustration of a strong mascot holding a large green leaf"></div>
</section>

<div class="abs logo">Otter Bites</div>
<nav class="abs nav"><span>Home</span><span>Shop</span><span>About</span><span>Contact</span></nav>
<div class="abs icons">
  <svg width="28" height="28" viewBox="0 0 28 28" fill="none" stroke="#046a04" stroke-width="1.8"><circle cx="12" cy="12" r="9"/><line x1="19" y1="19" x2="26" y2="26"/></svg>
  <svg width="28" height="28" viewBox="0 0 28 28" fill="none" stroke="#046a04" stroke-width="1.8"><circle cx="14" cy="9" r="6"/><path d="M3 27c0-7 5-11 11-11s11 4 11 11"/></svg>
  <svg width="28" height="28" viewBox="0 0 28 28" fill="none" stroke="#046a04" stroke-width="1.8"><path d="M2 6h4l3 13h14l3-10H8"/><circle cx="11" cy="24" r="2"/><circle cx="21" cy="24" r="2"/></svg>
</div>
<div class="cart-count">0</div>

<h1 class="abs hero-title">NATURAL<br>SUPPLEMENTS</h1>
<p class="abs hero-sub">Boost your health and live a<br>better life.</p>
<div class="abs btn hero-btn">Shop now</div>

<svg class="abs perks" width="1200" height="113">
  <polygon points="0,0 398,0 327,113 0,113" fill="#046a04"/>
  <polygon points="870,0 1200,0 1200,113 801,113" fill="#046a04"/>
</svg>
<div class="perk" style="left:19px;color:#fff">Free Shipping</div>
<div class="perk" style="left:420px;color:#046a04">Worldwide Shipping</div>
<div class="perk" style="left:855px;top:636px;color:#fff">Free Samples</div>

<div class="cat" style="left:150px;background:linear-gradient(160deg,#6e5a68,#5c4d5b)" role="img" aria-label="Photo of scattered capsules">
  <div class="cat-label">Immune System Boosters</div></div>
<div class="cat" style="left:454px;background:linear-gradient(180deg,#b97f10,#a97a18 50%,#b08a2a)" role="img" aria-label="Photo of golden softgel vitamins">
  <div class="cat-label" style="top:130px">Vitamins</div></div>
<div class="cat" style="left:757px;background:linear-gradient(180deg,#7a3a66,#862f66)" role="img" aria-label="Photo of green and white capsules">
  <div class="cat-label">Workout Supplements</div></div>

<div class="abs tabs">
  <div class="tab active" style="left:150px">Top Sellers</div>
  <div class="tab" style="left:450px;width:300px">New Arrivals</div>
  <div class="tab" style="left:750px">On Sale</div>
</div>

<div class="card" style="left:150px;top:1188px">
  <div class="card-img"><div class="bottle orange" role="img" aria-label="Orange supplement bottle"></div></div>
  <div class="card-title">Vitamin C</div><div class="card-price">$20.00</div>
  <p class="card-desc">Lorem ipsum dolor sit amet, consectetur elit. Morbi pellentesque, nisi ac tincidunt varius, erat nulla tempor est, ac malesuada ex quam sit amet ipsum.</p>
  <div class="rating"><svg width="96" height="16" viewBox="0 0 96 16" fill="#f5b300"><path id="s" d="M8 1l2.1 4.6 5 .5-3.8 3.3 1.1 4.9L8 11.8 3.6 14.3l1.1-4.9L.9 6.1l5-.5z"/><use href="#s" x="19"/><use href="#s" x="38"/><use href="#s" x="57"/><use href="#s" x="76"/></svg>4.86 (80)</div>
  <div class="btn card-btn">Add to cart</div>
</div>
<div class="card" style="left:454px;top:1188px">
  <div class="card-img"><div class="bottle orange" role="img" aria-label="Orange supplement bottle"></div></div>
  <div class="card-title">Vitamin D3</div><div class="card-price">$22.00</div>
  <p class="card-desc">Lorem ipsum dolor sit amet, consectetur elit. Morbi pellentesque, nisi ac tincidunt varius, erat nulla tempor est, ac malesuada ex quam sit amet ipsum.</p>
  <div class="rating"><svg width="96" height="16" viewBox="0 0 96 16" fill="#f5b300"><use href="#s"/><use href="#s" x="19"/><use href="#s" x="38"/><use href="#s" x="57"/><use href="#s" x="76"/></svg>4.70 (85)</div>
  <div class="btn card-btn">Add to cart</div>
</div>
<div class="card" style="left:757px;top:1188px">
  <div class="card-img"><div class="bottle yellow" role="img" aria-label="Yellow supplement tub"></div></div>
  <div class="card-title">Pre Workout</div><div class="card-price">$30.00</div>
  <p class="card-desc">Lorem ipsum dolor sit amet, consectetur elit. Morbi pellentesque, nisi ac tincidunt varius, erat nulla tempor est, ac malesuada ex quam sit amet ipsum.</p>
  <div class="rating"><svg width="96" height="16" viewBox="0 0 96 16" fill="#f5b300"><use href="#s"/><use href="#s" x="19"/><use href="#s" x="38"/><use href="#s" x="57"/><use href="#s" x="76"/></svg>4.69 (90)</div>
  <div class="btn card-btn">Add to cart</div>
</div>
<div class="card" style="left:150px;top:1615px">
  <div class="card-img"><div class="bottle yellow" style="left:100px" role="img" aria-label="Yellow supplement tub"></div></div>
  <div class="card-title">Post Workout</div><div class="card-price">$28.00</div>
  <p class="card-desc">Lorem ipsum dolor sit amet, consectetur elit. Morbi pellentesque, nisi ac tincidunt varius, erat nulla tempor est, ac malesuada ex quam sit amet ipsum.</p>
  <div class="rating"><svg width="96" height="16" viewBox="0 0 96 16" fill="#f5b300"><use href="#s"/><use href="#s" x="19"/><use href="#s" x="38"/><use href="#s" x="57"/><use href="#s" x="76"/></svg>4.69 (95)</div>
  <div class="btn card-btn">Add to cart</div>
</div>
<div class="card" style="left:454px;top:1615px">
  <div class="card-img"><div class="bottle orange" role="img" aria-label="Orange supplement bottle"></div></div>
  <div class="card-title">Hair, Skin &amp; Nails</div><div class="card-price">$34.00</div>
  <p class="card-desc">Lorem ipsum dolor sit amet, consectetur elit. Morbi pellentesque, nisi ac tincidunt varius, erat nulla tempor est, ac malesuada ex quam sit amet ipsum.</p>
  <div class="rating"><svg width="96" height="16" viewBox="0 0 96 16" fill="#f5b300"><use href="#s"/><use href="#s" x="19"/><use href="#s" x="38"/><use href="#s" x="57"/><use href="#s" x="76"/></svg>4.89 (75)</div>
  <div class="btn card-btn">Add to cart</div>
</div>
<div class="card" style="left:757px;top:1615px">
  <div class="card-img"><div class="bottle orange" role="img" aria-label="Orange supplement bottle"></div></div>
  <div class="card-title">Zinc</div><div class="card-price">$20.00</div>
  <p class="card-desc">Lorem ipsum dolor sit amet, consectetur elit. Morbi pellentesque, nisi ac tincidunt varius, erat nulla tempor est, ac malesuada ex quam sit amet ipsum.</p>
  <div class="rating"><svg width="96" height="16" viewBox="0 0 96 16" fill="#f5b300"><use href="#s"/><use href="#s" x="19"/><use href="#s" x="38"/><use href="#s" x="57"/><use href="#s" x="76"/></svg>4.66 (60)</div>
  <div class="btn card-btn">Add to cart</div>
</div>

<section class="abs news"></section>
<div class="abs news-art" role="img" aria-label="Illustration of the mascot peeking in"></div>
<h2 class="abs news-title">Stay Updated</h2>
<p class="abs news-sub">Subscribe to our newsletter and get the latest news and offers.</p>
<div class="abs news-input">Enter your e-mail address</div>
<div class="abs btn news-btn">Subscribe</div>

<div class="abs foot-logo">Otter Bites</div>
<p class="abs foot-about">Lorem ipsum dolor sit amet, consectetur adipiscing elit. Morbi pellentesque, nisi ac tincidunt varius, erat nulla tempor est, ac malesuada ex quam sit amet ipsum.</p>
<div class="abs foot-h" style="left:555px;top:2286px">Navigation</div>
<div class="abs foot-links" style="left:555px;top:2314px">Home<br>Shop<br>About<br>Contact</div>
<div class="abs foot-links" style="left:640px;top:2314px">Privacy Policy<br>Returns &amp; Refunds<br>FAQs</div>
<div class="abs foot-h" style="left:926px;top:2286px">Keep Connected</div>
<div class="abs social"><span aria-label="Social link"></span><span aria-label="Social link"></span><span aria-label="Social link"></span></div>
<div class="abs copyright">Otter Bites 2020 All Rights Reserved.</div>

</body>
</html>
```